Brightwell Giving Inc

We need a full re-design of our non-profit organization website (www.brightwellgiving.org). Ideally, we are looking to make it more attractive, user-friendly, and interactive with our business model.

Please make sure to user colors that ago with our logo.

We need a homepage done and we also need a content page done where we will use for the other pages to fill with content.

Target Market(s)

Clothes/textiles donations.

Industry/Entity Type

Charity

Number of Pages Required

2 page

Colors

Designer to choose colors to be used in the design.

Requirements
Must have
• It must match the styling of our logo and same colors as current website. (www.brightwellgiving.org)
Nice to have
• Sleek homepage that is easy to understand and get our main points across.

```html
<!DOCTYPE html>
<html lang="en">
<head>
<meta charset="utf-8">
<title>Brightwell Giving</title>
<link rel="stylesheet" href="https://fonts.googleapis.com/css2?family=Crimson+Text:ital,wght@0,400;0,600;1,400&family=Lato:wght@400;700&display=swap">
<style>
:root{
  --green:#77b94a;
  --green-dark:#5e9c36;
  --green-pale:#e6f1dc;
  --ink:#333;
  --muted:#777;
  --line:#ddd;
  --field:#ececec;
  --grey-band:#efefef;
  --white:#fff;
}
*{box-sizing:border-box;margin:0;padding:0}
html,body{width:1200px;height:4110px;overflow:hidden}
body{font-family:"Lato",sans-serif;color:var(--ink);background:var(--white);position:relative}
.serif{font-family:"Crimson Text",serif}
.wrap{position:absolute;left:77px;width:1046px}

/* header */
.site-header{position:absolute;top:0;left:0;width:1200px;height:110px;background:var(--white);z-index:2}
.brand{position:absolute;left:77px;top:28px;display:flex;align-items:center;gap:14px}
.brand-mark{width:42px;height:42px;background:var(--green)}
.brand-name{font-size:26px;font-weight:700;color:var(--ink)}
.brand-tag{position:absolute;left:56px;top:42px;font-size:13px;color:var(--muted);white-space:nowrap}
.contact-item{position:absolute;top:26px;display:flex;gap:16px;align-items:center}
.contact-item .icon{width:54px;height:54px;border:2px solid var(--green);border-radius:50%;display:flex;align-items:center;justify-content:center}
.contact-item .label{font-size:17px;color:var(--muted)}
.contact-item .value{font-size:18px;color:var(--ink);margin-top:4px}
.main-nav{position:absolute;top:110px;left:77px;width:1046px;height:50px;background:var(--green);display:flex;align-items:center;padding-left:22px;gap:36px;z-index:2}
.main-nav a{color:var(--white);text-decoration:none;font-size:15px;font-weight:700;letter-spacing:.5px}

/* hero */
.hero{position:absolute;top:110px;left:0;width:1200px;height:630px;background:linear-gradient(120deg,#e9ddd6,#f3ece7 40%,#ddd5d0 70%,#c9c3bf)}
.hero-text{position:absolute;top:282px;left:0;width:1200px;text-align:center}
.hero-text h1{font-family:"Crimson Text",serif;font-weight:400;font-size:46px;letter-spacing:1px;color:#222}
.hero-text p{width:700px;margin:14px auto 0;font-size:15.5px;line-height:1.7;color:#333}

/* welcome */
.welcome{position:absolute;top:740px;left:0;width:1200px;height:520px}
.welcome-head{position:absolute;left:117px;top:190px;width:276px;text-align:center}
.welcome-head h2{font-family:"Crimson Text",serif;font-weight:600;font-size:44px;color:var(--green)}
.welcome-head p{font-family:"Crimson Text",serif;font-style:italic;font-size:19px;color:var(--muted);line-height:1.4;margin-top:8px}
.welcome-head .rule{width:48px;height:2px;background:var(--green);margin:18px auto 0}
.welcome-photo{position:absolute;left:455px;top:76px;width:290px;height:368px;border-radius:12px;background:linear-gradient(160deg,#c8d2da,#e8d4c4 55%,#b89270)}
.welcome-copy{position:absolute;left:803px;top:84px;width:320px;font-size:14.5px;line-height:1.75;color:#555}
.welcome-copy p+p{margin-top:12px}
.welcome-copy .more{font-style:italic;color:#444}

/* search band */
.finder{position:absolute;top:1260px;left:0;width:1200px;height:115px;background:var(--green)}
.finder h3{position:absolute;left:82px;top:36px;font-size:34px;font-style:italic;font-weight:700;color:var(--white)}
.finder .zip{position:absolute;left:602px;top:40px;width:356px;height:42px;border:1.5px solid var(--white);color:var(--white);font-size:14px;padding:12px 18px}
.finder .btn{position:absolute;left:966px;top:40px;width:157px;height:42px;background:var(--white);color:var(--green);font-size:19px;font-weight:700;text-align:center;line-height:42px}

/* section titles */
.sec-title{position:absolute;left:0;width:1200px;text-align:center}
.sec-title h2{font-family:"Crimson Text",serif;font-weight:600;font-size:44px;color:var(--green);letter-spacing:1px}
.sec-title p{font-family:"Crimson Text",serif;font-style:italic;font-size:17px;color:#555;letter-spacing:.6px;margin-top:0}

/* how it works */
.how{position:absolute;top:1375px;left:0;width:1200px;height:466px}
.how .track{position:absolute;top:242px;left:219px;width:751px;height:2px;background:var(--line)}
.how .dot{position:absolute;top:237px;width:12px;height:12px;border-radius:50%;background:var(--green)}
.step{position:absolute;top:176px;width:300px;text-align:center}
.step .ring{width:134px;height:134px;border-radius:50%;border:2px solid #ccc;margin:0 auto;display:flex;align-items:center;justify-content:center;background:var(--white)}
.step .ring span{width:110px;height:110px;border-radius:50%;border:5px solid var(--green-pale);display:flex;align-items:center;justify-content:center}
.step p{margin-top:38px;font-size:19px;line-height:1.6;color:#444}

/* testimonials */
.testimonials{position:absolute;top:1841px;left:0;width:1200px;height:474px;background:linear-gradient(135deg,#8cc75f,#7ab84e 50%,#8bc55e);color:var(--white);text-align:center}
.testimonials h2{font-family:"Crimson Text",serif;font-weight:600;font-size:44px;margin-top:56px;letter-spacing:1px}
.testimonials .sub{font-family:"Crimson Text",serif;font-style:italic;font-size:17px;letter-spacing:.6px}
.avatar{width:90px;height:90px;border-radius:50%;border:4px solid var(--white);background:#c7a788;margin:18px auto 0}
.testimonials .quote{width:860px;margin:30px auto 0;font-size:14.5px;line-height:1.8}
.testimonials .who{margin-top:20px;font-size:15px}
.arrow{position:absolute;top:250px}

/* news */
.news{position:absolute;top:2315px;left:0;width:1200px;height:672px}
.card{position:absolute;top:151px;width:323px;height:447px;border:1px solid var(--line);background:var(--white)}
.card .photo{height:234px;position:relative}
.card .date{position:absolute;left:0;bottom:0;background:var(--green);color:var(--white);font-size:14px;font-weight:700;padding:8px 12px}
.card h4{margin:24px 16px 0;font-size:17px;line-height:1.5;font-weight:700}
.card p{margin:12px 16px 0;font-size:14px;line-height:1.6;color:#666}
.card .read{display:inline-block;margin:12px 16px 0;font-size:13px;color:#444;text-decoration:underline}

/* donation levels */
.levels{position:absolute;top:2987px;left:0;width:1200px;height:619px;background:var(--grey-band)}
.level{position:absolute;top:164px;width:189px;height:247px;background:var(--white);text-align:center}
.level .cap{height:55px;background:var(--green);color:var(--white);font-family:"Crimson Text",serif;font-size:20px;padding-top:12px}
.level .num{width:80px;height:80px;border-radius:50%;background:var(--green);border:5px solid var(--white);color:var(--white);font-size:30px;line-height:70px;margin:-28px auto 0;box-shadow:0 0 0 2px var(--green-pale)}
.level .amt{margin-top:18px;font-size:21px;line-height:1.45;color:#555}
.levels .motto{position:absolute;top:456px;width:1200px;text-align:center;font-size:15px;color:#999}
.levels .btn{position:absolute;top:503px;left:520px;width:158px;height:48px;background:var(--green);color:var(--white);font-size:18px;font-weight:700;text-align:center;line-height:48px}

/* contact */
.contact{position:absolute;top:3606px;left:0;width:1200px;height:367px}
.contact .intro{position:absolute;top:118px;width:1200px;text-align:center;font-size:14px;font-style:italic;color:#666}
.field{position:absolute;background:var(--field);font-size:14px;color:#777;padding:12px 16px}
.submit{position:absolute;left:612px;top:322px;width:361px;height:42px;background:var(--green);color:var(--white);font-weight:700;font-size:17px;text-align:center;line-height:42px}

/* footer */
.site-footer{position:absolute;top:3973px;left:0;width:1200px;height:137px;background:var(--green);color:var(--white);text-align:center}
.foot-nav{display:flex;justify-content:center;gap:30px;margin-top:38px;font-size:14.5px}
.site-footer .copy{margin-top:28px;font-size:14px}
</style>
</head>
<body>

<header class="site-header">
  <div class="brand">
    <div class="brand-mark"></div>
    <div class="brand-name">BRIGHTWELL GIVING</div>
    <div class="brand-tag">Think Globally while Donating Locally</div>
  </div>
  <div class="contact-item" style="left:660px">
    <div class="icon"><svg width="26" height="26" viewBox="0 0 24 24"><path d="M6.6 10.8a15 15 0 0 0 6.6 6.6l2.2-2.2a1 1 0 0 1 1-.25 11.4 11.4 0 0 0 3.6.57 1 1 0 0 1 1 1V20a1 1 0 0 1-1 1A17 17 0 0 1 3 4a1 1 0 0 1 1-1h3.5a1 1 0 0 1 1 1c0 1.25.2 2.45.57 3.57a1 1 0 0 1-.25 1z" fill="#77b94a"/></svg></div>
    <div><div class="label">Toll Free</div><div class="value">(855) 410-7782</div></div>
  </div>
  <div class="contact-item" style="left:908px">
    <div class="icon"><svg width="26" height="26" viewBox="0 0 24 24"><path d="M6.6 10.8a15 15 0 0 0 6.6 6.6l2.2-2.2a1 1 0 0 1 1-.25 11.4 11.4 0 0 0 3.6.57 1 1 0 0 1 1 1V20a1 1 0 0 1-1 1A17 17 0 0 1 3 4a1 1 0 0 1 1-1h3.5a1 1 0 0 1 1 1c0 1.25.2 2.45.57 3.57a1 1 0 0 1-.25 1z" fill="#77b94a"/></svg></div>
    <div><div class="label">New York</div><div class="value">518-555-0193</div></div>
  </div>
</header>

<section class="hero" role="img" aria-label="Smiling volunteers sorting donated clothing together">
  <div class="hero-text">
    <h1>AN OPEN BOOK ORGANIZATION</h1>
    <p>We are a family based non-profit organization in the name of Brightwell Giving Inc. We started this foundation in effort to help the community and unite it's effort to give back to the less fortunate by the means of donating unwanted used clothing.</p>
  </div>
</section>

<nav class="main-nav">
  <a>HOME</a><a>ABOUT</a><a>MISSION</a><a>FAMILY</a><a>HOW IT WORKS</a><a>SPONSORS</a><a>NEWS</a><a>DONATE</a><a>WALL OF NEED</a>
</nav>

<section class="welcome">
  <div class="welcome-head">
    <h2>WELCOME</h2>
    <p>OUR GOAL IS TO BE WITH AND WITHIN THE COMMUNITY</p>
    <div class="rule"></div>
  </div>
  <div class="welcome-photo" role="img" aria-label="Volunteer holding up a donated blouse over a box of clothes"></div>
  <div class="welcome-copy">
    <p>Brightwell Giving is a non-profit organization that was created for one purpose: helping the less fortunate in our country's time of greatest need. Started in 2007, Brightwell Giving has been a dedicated member of its local communities over the past four years.</p>
    <p>The company's clothing collection efforts have allowed it to provide some of the neediest members of the community to clothe themselves and their families.</p>
    <p class="more">Learn more about us... &raquo;</p>
  </div>
</section>

<section class="finder">
  <h3>Find Local Donation Place</h3>
  <div class="zip">enter zipcode</div>
  <div class="btn">SEARCH</div>
</section>

<section class="how">
  <div class="sec-title" style="top:44px"><h2>HOW IT WORKS</h2><p>HELP DISASTER VICTIMS OF HURRICANE IRENE</p></div>
  <div class="track"></div>
  <div class="dot" style="left:372px"></div>
  <div class="dot" style="left:820px"></div>
  <div class="step" style="left:69px">
    <div class="ring"><span><svg width="56" height="56" viewBox="0 0 56 56"><rect x="12" y="10" width="32" height="6" rx="2" fill="#77b94a"/><path d="M14 18h28l-3 30H17z" fill="#77b94a"/><path d="M24 32l5-5 5 5M29 27v12" stroke="#fff" stroke-width="3" fill="none"/></svg></span></div>
    <p>Drop off clothing at your closest donation bin.</p>
  </div>
  <div class="step" style="left:453px">
    <div class="ring"><span><svg width="60" height="56" viewBox="0 0 60 56"><path d="M18 8l-12 8 5 8 5-3v8L8 46h44l-8-17v-8l5 3 5-8-12-8c-2 5-6 7-12 7s-10-2-12-7z" fill="#77b94a"/></svg></span></div>
    <p>We pick it up and take it to our sorting facility</p>
  </div>
  <div class="step" style="left:820px">
    <div class="ring"><span><svg width="56" height="56" viewBox="0 0 56 56"><rect x="16" y="6" width="26" height="44" rx="4" fill="none" stroke="#77b94a" stroke-width="4"/><circle cx="29" cy="44" r="2" fill="#77b94a"/><text x="29" y="33" font-family="Lato,sans-serif" font-size="18" font-weight="700" fill="#77b94a" text-anchor="middle">$</text></svg></span></div>
    <p>Charities get clothing. We pay you for the clothes.</p>
  </div>
</section>

<section class="testimonials" role="group" aria-label="Testimonials">
  <h2>TESTIMONIALS</h2>
  <div class="sub">SUPPORT ANTI-GUN VIOLENCE</div>
  <div class="avatar" role="img" aria-label="Portrait of the reviewer"></div>
  <p class="quote">Lorem Ipsum is simply dummy text of the printing and typesetting industry. Lorem Ipsum has been the industry's standard dummy text ever since the 1500s, when an unknown printer took a galley of type and scrambled it to make a type specimen book. It has survived not only five centuries, but also the leap into electronic typesetting.</p>
  <div class="who">- Name Surname</div>
  <svg class="arrow" style="left:80px" width="20" height="36" viewBox="0 0 20 36"><path d="M17 3L3 18l14 15" stroke="#fff" stroke-width="3" fill="none"/></svg>
  <svg class="arrow" style="left:1100px" width="20" height="36" viewBox="0 0 20 36"><path d="M3 3l14 15L3 33" stroke="#fff" stroke-width="3" fill="none"/></svg>
</section>

<section class="news">
  <div class="sec-title" style="top:40px"><h2>LATEST NEWS</h2><p>HELP VALLEY PARENT &amp; CHILD ALLIANCE</p></div>
  <article class="card" style="left:77px">
    <div class="photo" role="img" aria-label="Volunteers handing out donated clothes to a child" style="background:linear-gradient(135deg,#b79a86,#e7ddd5 55%,#8d7b6c)"><span class="date">26 Jan 2018</span></div>
    <h4>Lorem Ipsum is simply dummy text of the printing.</h4>
    <p>Lorem Ipsum is simply dummy text of the printing and typesetting industry. Lorem Ipsum has been the industry's standard.</p>
    <a class="read">READ MORE</a>
  </article>
  <article class="card" style="left:438px">
    <div class="photo" role="img" aria-label="Volunteers in white shirts sorting clothes on a rack" style="background:linear-gradient(135deg,#9fb5c7,#e4e8ec 55%,#7d8f9c)"><span class="date">26 Jan 2018</span></div>
    <h4>Lorem Ipsum is simply dummy text of the printing.</h4>
    <p>Lorem Ipsum is simply dummy text of the printing and typesetting industry. Lorem Ipsum has been the industry's standard.</p>
    <a class="read">READ MORE</a>
  </article>
  <article class="card" style="left:800px">
    <div class="photo" role="img" aria-label="Group of volunteers carrying donation boxes outdoors" style="background:linear-gradient(135deg,#c2a14a,#8a9a52 50%,#b65a3c)"><span class="date">26 Jan 2018</span></div>
    <h4>Lorem Ipsum is simply dummy text of the printing.</h4>
    <p>Lorem Ipsum is simply dummy text of the printing and typesetting industry. Lorem Ipsum has been the industry's standard.</p>
    <a class="read">READ MORE</a>
  </article>
</section>

<section class="levels">
  <div class="sec-title" style="top:50px"><h2>DONATION RECEPIENTS</h2><p>HELP DISASTER VICTIMS OF HURRICANE IRENE</p></div>
  <div class="level" style="left:77px"><div class="cap">LEVEL</div><div class="num">01</div><div class="amt">1000</div></div>
  <div class="level" style="left:291px"><div class="cap">LEVEL</div><div class="num">02</div><div class="amt">$1000<br>&ndash;<br>$2500</div></div>
  <div class="level" style="left:505px"><div class="cap">LEVEL</div><div class="num">03</div><div class="amt">$2500<br>&ndash;<br>$5000</div></div>
  <div class="level" style="left:719px"><div class="cap">LEVEL</div><div class="num">04</div><div class="amt">$5000<br>&ndash;<br>$10,000</div></div>
  <div class="level" style="left:934px"><div class="cap">LEVEL</div><div class="num">05</div><div class="amt">$10,000<br>&ndash;<br>$25,000</div></div>
  <div class="motto">Think Globally while Donating Locally</div>
  <div class="btn">READ MORE</div>
</section>

<section class="contact">
  <div class="sec-title" style="top:48px"><h2>CONTACT US</h2></div>
  <p class="intro">Please tell us, what kind of help do you need and we will try to help you with Gods help.</p>
  <div class="field" style="left:227px;top:160px;width:362px;height:42px">Name</div>
  <div class="field" style="left:227px;top:214px;width:362px;height:42px">Email</div>
  <div class="field" style="left:227px;top:268px;width:362px;height:42px">Phone</div>
  <div class="field" style="left:612px;top:160px;width:361px;height:96px">Message</div>
  <div class="submit">SUBMIT</div>
</section>

<footer class="site-footer">
  <nav class="foot-nav"><a>Home</a><a>About</a><a>Mission</a><a>Family</a><a>How it works</a><a>Sponsor</a><a>News</a><a>Donate</a><a>Wall of Need</a><a>Donation in Europa</a></nav>
  <div class="copy">&copy; 2018 Brightwell Giving. All Rights Reserved</div>
</footer>

</body>
</html>
```